Trade show post card for sportfishing

I would like a double sided postcard used to be a larger more descriptive, eye catching, marketing tool to be used at trade show. I want the double sided postcard to be descriptive and eye catching for both avid fisherman and inviting enough not to scare away first timers looking to enjoy the experience.

Target Market(s)

Males 25-60

Colors

Designer to choose colors to be used in the design.

Requirements
Must have
• My logo, website, phone number, type of trips, pictures of fishing trips we have had which I included below. But I do not need all of the pictures designers can use ones they feel will be most appealing
Nice to have
• Color scheme that works with my logo.

```html
<!DOCTYPE html>
<html lang="en">
<head>
<meta charset="utf-8">
<title>Tight Line Charters – Trade Show Postcard</title>
<link href="https://fonts.googleapis.com/css2?family=Bebas+Neue&family=Roboto:wght@400;700&display=swap" rel="stylesheet">
<style>
  :root{
    --page:#e6e6e6;
    --card:#0b0b0b;
    --green:#6cc644;
    --green-dark:#3f8f22;
    --white:#ffffff;
    --water:#6f8796;
    --boat:#a9b0b3;
    --night:#1c1c22;
  }
  *{box-sizing:border-box;margin:0;padding:0}
  html,body{width:1200px;height:1000px;overflow:hidden;background:var(--page);font-family:"Roboto",Arial,sans-serif}
  .card{position:absolute;left:280px;width:640px;height:390px;background:var(--card);overflow:hidden;box-shadow:0 4px 14px rgba(0,0,0,.25)}
  .card--front{top:70px}
  .card--back{top:510px}
  .photo{position:absolute;border:2px solid #ddd}
  .photo--night{background:linear-gradient(180deg,var(--night),#3a3d44)}
  .photo--river{background:linear-gradient(180deg,#b9cde0 0%,var(--water) 45%,#49545a 100%)}
  .photo--deck{background:linear-gradient(180deg,#c7d3dc 0%,var(--boat) 50%,#5b6064 100%)}
  .photo--dock{background:linear-gradient(180deg,#5f7d4b 0%,#8a9a8a 50%,#4b4f52 100%)}
  .curves{position:absolute;left:0;top:0;width:640px;height:390px}
  .call-pill{position:absolute;left:70px;top:175px;height:42px;padding:0 14px;border:2px solid var(--white);border-radius:22px;background:var(--green);display:flex;align-items:center;gap:10px;color:var(--white)}
  .call-label{font-family:"Bebas Neue",Arial,sans-serif;font-size:30px;letter-spacing:.5px;line-height:1}
  .call-number{font-family:"Bebas Neue",Arial,sans-serif;font-size:30px;line-height:1;display:flex;align-items:center;gap:4px}
  .phone-icon{width:20px;height:20px}
  .website{position:absolute;color:var(--white);font-weight:700;font-size:15px}
  .website b{color:var(--green)}
  .card--front .website{left:120px;top:226px}
  .brand{position:absolute;display:flex;align-items:center;gap:8px;color:var(--green);font-weight:700;font-family:"Roboto",Arial,sans-serif}
  .brand-dot{width:14px;height:14px;border-radius:50%;background:var(--green)}
  .card--front .brand{left:440px;top:170px;font-size:24px}
  .benefits{position:absolute;left:40px;top:22px;right:30px;list-style:none;color:var(--white);font-weight:700;font-size:11px;line-height:1.35;z-index:2}
  .benefits li{display:flex;gap:8px;margin-bottom:6px}
  .benefits .hl{color:var(--green)}
  .tick{flex:0 0 12px;width:12px;height:12px;margin-top:1px}
  .strip{position:absolute;left:30px;right:0;top:215px;height:140px}
  .strip .photo{top:0;height:140px;border:none}
  .strip-fade{position:absolute;left:0;right:0;top:215px;height:175px;background:linear-gradient(180deg,var(--card) 0%,rgba(11,11,11,0) 15%,rgba(11,11,11,0) 42%,var(--card) 78%)}
  .back-call{position:absolute;left:250px;top:298px;color:var(--white);display:flex;align-items:center;gap:12px}
  .back-call .call-number{color:var(--green)}
  .card--back .website{left:250px;top:332px;font-size:16px}
  .social{position:absolute;left:300px;top:356px;display:flex;align-items:center;gap:6px;color:var(--white);font-size:13px}
  .social-dot{width:14px;height:14px;border-radius:50%;background:var(--green)}
  .card--back .brand{left:100px;top:330px;font-size:20px}
</style>
</head>
<body>

<section class="card card--front" aria-label="Postcard front">
  <div class="photo photo--night" style="left:8px;top:40px;width:190px;height:150px" role="img" aria-label="Angler holding a striped bass at night"></div>
  <div class="photo photo--river" style="left:198px;top:22px;width:190px;height:150px" role="img" aria-label="Angler in a cap holding a striped bass on the river"></div>
  <div class="photo photo--river" style="left:388px;top:0;width:252px;height:130px" role="img" aria-label="Young woman holding a striped bass aboard the boat"></div>

  <div class="photo photo--dock" style="left:0;top:250px;width:215px;height:140px" role="img" aria-label="Angler on the dock holding a large striped bass"></div>
  <div class="photo photo--deck" style="left:215px;top:240px;width:200px;height:150px" role="img" aria-label="Group of anglers on deck showing their catch"></div>
  <div class="photo photo--deck" style="left:415px;top:240px;width:225px;height:150px" role="img" aria-label="Angler in a cap holding a striped bass on the boat"></div>

  <svg class="curves" viewBox="0 0 640 390" aria-hidden="true">
    <path d="M0 200 Q240 190 420 150 T640 60 L640 290 Q420 225 200 250 T0 250 Z" fill="var(--card)"/>
    <path d="M0 200 Q240 190 420 150 T640 60" fill="none" stroke="var(--green)" stroke-width="3"/>
    <path d="M200 246 Q420 222 640 288" fill="none" stroke="var(--green)" stroke-width="3"/>
  </svg>

  <div class="call-pill">
    <span class="call-label">Call Now</span>
    <span class="call-number">
      <svg class="phone-icon" viewBox="0 0 24 24" aria-hidden="true"><path fill="#fff" d="M6.6 10.8a15 15 0 0 0 6.6 6.6l2.2-2.2c.3-.3.7-.4 1-.2 1.1.4 2.3.6 3.6.6.6 0 1 .4 1 1V20c0 .6-.4 1-1 1A17 17 0 0 1 3 4c0-.6.4-1 1-1h3.5c.6 0 1 .4 1 1 0 1.2.2 2.4.6 3.6.1.3 0 .7-.2 1z"/></svg>
      555 014 2290
    </span>
  </div>
  <p class="website">www.<b>tightlinecharters</b>.com</p>

  <div class="brand"><span class="brand-dot"></span>Tight Line Charters</div>
</section>

<section class="card card--back" aria-label="Postcard back">
  <div class="strip">
    <div class="photo photo--river" style="left:0;width:210px" role="img" aria-label="Anglers on board holding a striped bass"></div>
    <div class="photo photo--deck" style="left:210px;width:200px" role="img" aria-label="Group of anglers lined up with their catch at the marina"></div>
    <div class="photo photo--river" style="left:410px;width:200px" role="img" aria-label="Family with kids holding a striped bass on the boat"></div>
  </div>
  <div class="strip-fade"></div>

  <ul class="benefits">
    <li><svg class="tick" viewBox="0 0 12 12" aria-hidden="true"><circle cx="6" cy="6" r="5" fill="none" stroke="var(--green)" stroke-width="1.4"/><path d="M3.5 6.2l1.7 1.7 3.3-3.4" fill="none" stroke="var(--green)" stroke-width="1.4"/></svg><span><span class="hl">Tight Line Charters</span> offers half and full day charters on the <span class="hl">Hudson River during April and May sailing from Poughkeepsie NY</span>.</span></li>
    <li><svg class="tick" viewBox="0 0 12 12" aria-hidden="true"><circle cx="6" cy="6" r="5" fill="none" stroke="var(--green)" stroke-width="1.4"/><path d="M3.5 6.2l1.7 1.7 3.3-3.4" fill="none" stroke="var(--green)" stroke-width="1.4"/></svg><span>Come aboard our <span class="hl">27 foot Marlo</span> walk around style fishing hull powered by <span class="hl">twin 200 Horsepower engines</span> with a working head, cabin, and full enclosure to get out of the elements.</span></li>
    <li><svg class="tick" viewBox="0 0 12 12" aria-hidden="true"><circle cx="6" cy="6" r="5" fill="none" stroke="var(--green)" stroke-width="1.4"/><path d="M3.5 6.2l1.7 1.7 3.3-3.4" fill="none" stroke="var(--green)" stroke-width="1.4"/></svg><span>We have the best electronics on the market by <span class="hl">Navtrek</span> to maximize our fish finding capability and safe navigation.</span></li>
    <li><svg class="tick" viewBox="0 0 12 12" aria-hidden="true"><circle cx="6" cy="6" r="5" fill="none" stroke="var(--green)" stroke-width="1.4"/><path d="M3.5 6.2l1.7 1.7 3.3-3.4" fill="none" stroke="var(--green)" stroke-width="1.4"/></svg><span><span class="hl">Targeting Striped Bass</span> during their spring migration up the Hudson River</span></li>
    <li><svg class="tick" viewBox="0 0 12 12" aria-hidden="true"><circle cx="6" cy="6" r="5" fill="none" stroke="var(--green)" stroke-width="1.4"/><path d="M3.5 6.2l1.7 1.7 3.3-3.4" fill="none" stroke="var(--green)" stroke-width="1.4"/></svg><span><span class="hl">Captain Dan Mercer</span> is a <span class="hl">USCG Licensed</span> Captain with over 25 years of experience fishing the Hudson River for Striped Bass.</span></li>
    <li><svg class="tick" viewBox="0 0 12 12" aria-hidden="true"><circle cx="6" cy="6" r="5" fill="none" stroke="var(--green)" stroke-width="1.4"/><path d="M3.5 6.2l1.7 1.7 3.3-3.4" fill="none" stroke="var(--green)" stroke-width="1.4"/></svg><span>Kid and beginner friendly</span></li>
  </ul>

  <div class="back-call">
    <span class="call-label">Call Now</span>
    <span class="call-number">
      <svg class="phone-icon" viewBox="0 0 24 24" aria-hidden="true"><path fill="var(--green)" d="M6.6 10.8a15 15 0 0 0 6.6 6.6l2.2-2.2c.3-.3.7-.4 1-.2 1.1.4 2.3.6 3.6.6.6 0 1 .4 1 1V20c0 .6-.4 1-1 1A17 17 0 0 1 3 4c0-.6.4-1 1-1h3.5c.6 0 1 .4 1 1 0 1.2.2 2.4.6 3.6.1.3 0 .7-.2 1z"/></svg>
      555 014 2290
    </span>
  </div>
  <p class="website">www.<b>tightlinecharters</b>.com</p>
  <div class="social"><span class="social-dot"></span><span class="social-dot"></span>@tightlinecharters</div>

  <div class="brand"><span class="brand-dot"></span>Tight Line</div>
</section>

</body>
</html>
```